Business Card Design

I give lessons and clinics for dressage riders
I would like the design to be an outline (with broad lines) of a dressage horse and rider with in background of whole card with print over top tan or parchment card with burgundy print

Industry/Entity Type

Business

Contact Information for Business Card

Tod Harlick
555-317-0492
Classical dressage training for the modern American
Clinics, lessons, training level -Prix St. George

Requirements
Must have
• broad lined outline of dressage horse and rider

```html
<!DOCTYPE html>
<html lang="en">
<head>
<meta charset="utf-8">
<title>Tod Harlick — Business Card</title>
<link rel="stylesheet" href="https://fonts.googleapis.com/css2?family=Cinzel:wght@400;500&family=Arimo:wght@400&display=swap">
<style>
  :root {
    --backdrop: #e6e0d6;
    --card: #4a111f;
    --figure-tone: #5c1d2d;
    --figure-edge: #531727;
    --ink: #ffffff;
  }
  * { box-sizing: border-box; margin: 0; padding: 0; }
  html, body {
    width: 1200px;
    height: 870px;
    overflow: hidden;
    background: var(--backdrop);
  }
  .canvas {
    width: 1200px;
    height: 870px;
    display: flex;
    align-items: center;
    justify-content: center;
  }
  .business-card {
    position: relative;
    width: 446px;
    height: 780px;
    background: var(--card);
    box-shadow: 0 6px 22px rgba(40, 20, 20, 0.25);
    color: var(--ink);
    text-align: center;
    overflow: hidden;
  }
  .rider-artwork {
    position: absolute;
    left: 70px;
    top: 60px;
    width: 306px;
    height: 690px;
    border-radius: 46% 46% 18% 18% / 22% 22% 8% 8%;
    background: linear-gradient(180deg, var(--figure-edge) 0%, var(--figure-tone) 35%, var(--figure-tone) 70%, var(--figure-edge) 100%);
  }
  .card-content {
    position: relative;
    padding-top: 116px;
  }
  .trainer-name {
    font-family: "Cinzel", "Times New Roman", serif;
    font-weight: 400;
    font-size: 36px;
    letter-spacing: 1.5px;
    line-height: 1;
  }
  .trainer-phone {
    font-family: "Arimo", Arial, sans-serif;
    font-size: 21px;
    letter-spacing: 0.5px;
    margin-top: 16px;
  }
  .tagline {
    font-family: "Arimo", Arial, sans-serif;
    font-size: 20px;
    line-height: 1.2;
    margin-top: 236px;
  }
  .services {
    list-style: none;
    font-family: "Arimo", Arial, sans-serif;
    font-size: 21px;
    margin-top: 14px;
  }
  .services li { line-height: 1.55; }
</style>
</head>
<body>
  <main class="canvas">
    <article class="business-card">
      <div class="rider-artwork" role="img" aria-label="Broad-line outline of a dressage horse and rider, printed faintly across the whole card behind the text"></div>
      <div class="card-content">
        <h1 class="trainer-name">Tod Harlick</h1>
        <p class="trainer-phone">555-317-0492</p>
        <p class="tagline">Classical dressage training for the<br>modern American Clinics</p>
        <ul class="services">
          <li>lessons</li>
          <li>training level</li>
          <li>Prix St. George</li>
        </ul>
      </div>
    </article>
  </main>
</body>
</html>
```